Communication of Recommended Belief Letter

To Whom This May Concern,

My company's name is Brookfane LLC. I would like to send electronic messages to my clients. Therefore, I would like PixelForge to create a letterhead template to say Brookfane- without the LLC. My messages could extend up to 20 pages long. I would like something that is chic, fancy, and has creative designs. The background color should be white. The creative designs are open for suggestions without color restrictions. Font type and color are also open for suggestions. It may be what you believe best suite's the letterhead. I would like the letterhead to include the company logo. Please see attachment for file. Thank you.

Target Market(s)

working class American's

Industry/Entity Type

Communication

Contact Information for Business Card

The business card should be chic and fancy.

Font styles to use
Script

Requirements
Must have
• Company name: Brookfane LLC
• Company symbol: Please see attachment
• Name: Moriel Haskins
• Title: President
• Company website: www.brookfanellc-example.com
Nice to have
• Open for suggestions

```html
<!DOCTYPE html>
<html lang="en">
<head>
<meta charset="UTF-8">
<title>Brookfane Letterhead</title>
<link rel="stylesheet" href="https://fonts.googleapis.com/css2?family=Arimo:wght@400;700&family=Cinzel:wght@400;600&family=Yellowtail&display=swap">
<style>
  :root {
    --backdrop: #ececec;
    --paper: #ffffff;
    --gold: #c9922a;
    --ink: #1a1a1a;
    --body-ink: #2b2b2b;
    --band-black: #0d0d0d;
    --watermark: #efe9df;
  }
  * { box-sizing: border-box; margin: 0; padding: 0; }
  html, body { width: 1200px; height: 795px; overflow: hidden; }
  body {
    background: var(--backdrop);
    font-family: "Arimo", Arial, sans-serif;
    color: var(--body-ink);
    position: relative;
  }
  .letterhead {
    position: absolute;
    left: 330px; top: 16px;
    width: 540px; height: 764px;
    background: var(--paper);
    box-shadow: 0 2px 10px rgba(0,0,0,0.12);
    overflow: hidden;
  }
  .watermark-art {
    position: absolute; left: 150px; top: 470px;
    width: 300px; height: 250px;
    border-radius: 50%;
    background: radial-gradient(ellipse at center, var(--watermark) 0%, rgba(239,233,223,0.6) 55%, rgba(255,255,255,0) 75%);
  }
  .wave {
    position: absolute; left: 0; top: 0;
    width: 540px; height: 764px;
  }
  .brand {
    position: absolute; left: 48px; top: 70px;
    display: flex; align-items: center; gap: 10px;
  }
  .brand-dot {
    width: 22px; height: 22px; border-radius: 50%;
    background: var(--gold);
  }
  .brand-name {
    font-family: "Cinzel", Georgia, serif;
    font-weight: 400;
    font-size: 26px;
    letter-spacing: 2px;
    color: var(--gold);
  }
  .sender {
    position: absolute; right: 40px; top: 46px;
    border-left: 1px solid var(--gold);
    padding-left: 8px;
    font-family: "Cinzel", Georgia, serif;
    font-size: 7px; line-height: 1.4;
    color: var(--ink);
  }
  .sender-name { font-size: 9px; font-weight: 600; color: var(--gold); }
  .sender-title { margin-bottom: 6px; }
  .recipient {
    position: absolute; left: 60px; top: 150px;
    font-size: 8px; line-height: 1.3; color: var(--ink);
  }
  .recipient-name { font-weight: 700; font-size: 9px; }
  .letter-body {
    position: absolute; left: 78px; top: 210px;
    width: 390px;
    font-size: 8.4px; line-height: 1.5;
  }
  .letter-body p { margin-bottom: 14px; }
  .signoff { margin-top: 2px; }
  .signature {
    position: absolute; left: 110px; top: 430px;
    font-family: "Yellowtail", "Brush Script MT", cursive;
    font-size: 34px; line-height: 1; color: var(--ink);
  }
  .signer {
    position: absolute; left: 128px; top: 476px;
    font-size: 8.5px; color: var(--ink);
  }
  .website {
    position: absolute; left: 390px; top: 712px;
    transform: rotate(-30deg);
    font-family: "Cinzel", Georgia, serif;
    font-size: 7px; color: var(--ink);
    white-space: nowrap;
  }
</style>
</head>
<body>
  <main class="letterhead">
    <div class="watermark-art" role="img" aria-label="Faint brand emblem watermark"></div>

    <svg class="wave" viewBox="0 0 540 764" aria-hidden="true">
      <path fill="var(--band-black)" d="M0,700 C120,745 300,770 420,712 C470,688 510,660 540,628 L540,648 C480,700 400,758 260,764 L90,764 C60,742 30,718 0,712 Z"/>
      <path fill="var(--gold)" d="M170,764 C310,762 430,725 540,656 L540,764 Z"/>
    </svg>

    <div class="brand">
      <span class="brand-dot"></span>
      <span class="brand-name">BROOKFANE</span>
    </div>

    <div class="sender">
      <div class="sender-name">Moriel Haskins</div>
      <div class="sender-title">President</div>
      <div>P.O Box 1750, Alder Creek</div>
      <div>Vermont 05612</div>
    </div>

    <div class="recipient">
      <div class="recipient-name">ARLEN VOSS</div>
      <div>Street Name City Name.</div>
      <div>Zip Coad 0000</div>
    </div>

    <section class="letter-body">
      <p>Lorem Ipsum is simply dummy text of the printing and typesetting industry. Lorem Ipsum has been the industry's standard dummy text ever since the 1500s, when an unknown printer took a galley of type and scrambled it to make a type specimen book. It has survived not only five centuries, but also the leap into electronic typesetting, remaining essentially unchanged. It was popularised in the 1960s with the release of Tessaprint sheets containing Lorem Ipsum passages, and more recently with desktop publishing software like Corvel PageSetter including versions of Lorem Ipsum.</p>
      <p>It is a long established fact that a reader will be distracted by the readable content of a page when looking at its layout. The point of using Lorem Ipsum is that it has a more-or-less normal distribution of letters, as opposed to using 'Content here, content here', making it look like readable English. Many desktop and web publishing packages and web page editors now use Lorem Ipsum as their default model text, and a search for 'lorem ipsum' will uncover many web sites still in their infancy. Various versions have evolved over the years, sometimes by accident, sometimes on purpose (injected humour and the like).</p>
      <div class="signoff">Regards,</div>
    </section>

    <div class="signature">Dane Corliss</div>
    <div class="signer">Dane Corliss</div>

    <div class="website">www.brookfanellc-example.com</div>
  </main>
</body>
</html>
```